Business Card Design Project

looking for business cards with new logo

I am looking to keep with the colors of the logo i posted.  Here are some other details to consider.  I would like my website prominently displayed on the business card with the logo.  my website is www.PRopelVK.com...it should be spelled this way.

My contact information is:

Daniel J Whitcombe III
Broker/Owner
4587 Larkspur Ave., Suite 308
Cedar Bluff, Ohio 44712
Office: 830-419-5576
Email:  Daniel@PRopelVK.com

Thank you
Daniel Whitcombe

```html
<!DOCTYPE html>
<html lang="en">
<head>
<meta charset="utf-8">
<title>Propel Realty – Business Cards</title>
<link rel="stylesheet" href="https://fonts.googleapis.com/css2?family=Mulish:wght@400;500&family=Open+Sans:wght@400;600&display=swap">
<style>
  :root {
    --backdrop: #dcd8d3;
    --card-white: #ffffff;
    --blue-deep: #124776;
    --blue-glow: #3aa2de;
    --brand-blue: #2b86c8;
    --ink-navy: #173e6b;
    --ink-gray: #8a8a8a;
    --rule-gray: #c9c9c9;
  }
  * { margin: 0; padding: 0; box-sizing: border-box; }
  html, body { width: 1200px; height: 789px; overflow: hidden; }
  body {
    position: relative;
    background: var(--backdrop);
    font-family: "Mulish", Arial, sans-serif;
  }
  .card {
    position: absolute;
    width: 406px;
    height: 228px;
    background: var(--card-white);
    box-shadow: 0 2px 6px rgba(0,0,0,.18);
  }
  .card--front-blue {
    left: 172px; top: 199px;
    background: radial-gradient(ellipse 60% 75% at 50% 42%, var(--blue-glow) 0%, #1f6aa6 45%, var(--blue-deep) 100%);
  }
  .card--back { left: 617px; top: 200px; width: 405px; height: 227px; }
  .card--front-white { left: 405px; top: 460px; }

  .brand-name {
    position: absolute;
    left: 0; right: 0;
    text-align: center;
    font-family: "Mulish", Arial, sans-serif;
    font-weight: 500;
    font-size: 30px;
    letter-spacing: .3px;
    color: var(--brand-blue);
  }
  .card--front-blue .brand-name { top: 90px; color: #ffffff; }
  .card--front-white .brand-name { top: 88px; }
  .card--back .brand-name { top: 50px; }

  .website {
    position: absolute;
    left: 0; right: 0;
    bottom: 12px;
    text-align: center;
    font-family: "Open Sans", Arial, sans-serif;
    font-weight: 600;
    font-size: 12.5px;
    color: var(--ink-navy);
  }
  .card--front-blue .website { color: #ffffff; }

  .contact-rule {
    position: absolute;
    left: 33px; width: 359px; top: 143px;
    border-top: 1px solid var(--rule-gray);
  }
  .holder {
    position: absolute;
    left: 49px; top: 157px;
    font-size: 11px;
    line-height: 14px;
    color: var(--ink-gray);
  }
  .contact-list {
    position: absolute;
    left: 218px; top: 150px;
    list-style: none;
    font-size: 11px;
    line-height: 14px;
    color: var(--ink-gray);
  }
  .contact-list li { display: flex; align-items: flex-start; white-space: nowrap; }
  .contact-list svg { width: 9px; height: 9px; margin: 3px 6px 0 0; flex: none; }
  .contact-list .indent { padding-left: 15px; }
</style>
</head>
<body>

  <section class="card card--front-blue">
    <p class="brand-name">Propel Realty</p>
    <p class="website">www.PRopelVK.com</p>
  </section>

  <section class="card card--back">
    <p class="brand-name">Propel Realty</p>
    <div class="contact-rule"></div>
    <p class="holder">Daniel J Whitcombe<br>Broker/Owner</p>
    <ul class="contact-list">
      <li>
        <svg viewBox="0 0 10 10" fill="none" stroke="#8a8a8a" stroke-width="1"><rect x="0.5" y="2" width="9" height="6.5"/><path d="M0.5 2 L5 5.8 L9.5 2"/></svg>
        4587 Larkspur Ave., Suite 308
      </li>
      <li class="indent">Cedar Bluff, Ohio 44712</li>
      <li>
        <svg viewBox="0 0 10 10" fill="none" stroke="#8a8a8a" stroke-width="1.1"><path d="M2.5 1 L4 3.3 L3 4.4 Q4.2 6.6 5.6 7 L6.7 6 L9 7.5 Q8.2 9.4 6.6 9 Q2 7.5 1 3.4 Q0.8 1.6 2.5 1 Z"/></svg>
        830-419-5576
      </li>
      <li>
        <svg viewBox="0 0 10 10" fill="none" stroke="#8a8a8a" stroke-width="1"><circle cx="5" cy="5" r="4.4"/><circle cx="5" cy="5" r="1.7"/><path d="M6.7 3.5 V6 Q6.7 7 7.6 7"/></svg>
        Daniel@PRopelVK.com
      </li>
    </ul>
  </section>

  <section class="card card--front-white">
    <p class="brand-name">Propel Realty</p>
    <p class="website">www.PRopelVK.com</p>
  </section>

</body>
</html>
```